Hacienda Valle Dorado Business cards

We would like 3 individual business cards with the logo you designed:

1) Marta Pellworth - Phone: 206 555 0147
2) Theodore K Pellworth - Phone 206 555 0183
3) Dana Whitlow - Phone 310-555-0126

Address for all three cards:
4217 288th Ave NE
Carnation, WA 98019
HaciendaValleDorado@mailbox-example.com

```html
<!DOCTYPE html>
<html lang="en">
<head>
<meta charset="utf-8">
<title>Hacienda Valle Dorado — Business Card</title>
<link rel="stylesheet" href="https://fonts.googleapis.com/css2?family=Crimson+Pro:wght@600&family=Pinyon+Script&display=swap">
<style>
  :root {
    --page-bg: #ffffff;
    --card-bg: #ffffff;
    --card-edge: #e6e6e6;
    --ink: #1c1d1c;
  }
  * { margin: 0; padding: 0; box-sizing: border-box; }
  html, body {
    width: 1200px;
    height: 1000px;
    overflow: hidden;
    background: var(--page-bg);
  }
  .canvas {
    position: relative;
    width: 1200px;
    height: 1000px;
  }
  .business-card {
    position: absolute;
    left: 175px;
    top: 263px;
    width: 851px;
    height: 474px;
    background: var(--card-bg);
    border: 2px solid var(--card-edge);
    color: var(--ink);
  }
  .brand-name {
    position: absolute;
    left: 70px;
    top: 255px;
    width: 330px;
    text-align: center;
    font-family: "Crimson Pro", Georgia, serif;
    font-weight: 600;
    font-size: 44px;
    line-height: 1.05;
    letter-spacing: 0.5px;
    color: var(--ink);
  }
  .contact-block {
    position: absolute;
    left: 439px;
    top: 80px;
    font-family: "Crimson Pro", Georgia, serif;
    font-weight: 600;
    color: var(--ink);
  }
  .person-name {
    font-family: "Pinyon Script", cursive;
    font-weight: 400;
    font-size: 46px;
    line-height: 1;
    margin-left: -6px;
    margin-bottom: 34px;
  }
  .phone {
    font-size: 27px;
    line-height: 1;
    margin-bottom: 40px;
  }
  .address-line {
    font-size: 27px;
    line-height: 39px;
  }
  .email {
    font-size: 21px;
    line-height: 39px;
  }
</style>
</head>
<body>
  <main class="canvas">
    <section class="business-card">
      <div class="brand-name">Hacienda<br>Valle Dorado</div>
      <div class="contact-block">
        <p class="person-name">Dana Whitlow</p>
        <p class="phone">PHONE: 310-555-0126</p>
        <address style="font-style: normal;">
          <p class="address-line">4217 288th Ave NE</p>
          <p class="address-line">Carnation, WA 98019</p>
          <p class="email">HaciendaValleDorado@mailbox-example.com</p>
        </address>
      </div>
    </section>
  </main>
</body>
</html>
```